I would like to start a new webpage for a dating site in switzerland.
The dating site is not a escort service at all and should not transmit any type of sexual connotation.
The is more a compagnionship dating : male pay to meet ladies for some time in which they invite them for dinner, coktail, museum visit or walking or even skying. the meeting will take place in big cities in switzerland: geneva, zurich, bern, lausannes.

```html
<!DOCTYPE html>
<html lang="en">
<head>
<meta charset="utf-8">
<title>Alpendate — Companionship Dating in Switzerland</title>
<link rel="stylesheet" href="https://fonts.googleapis.com/css2?family=Open+Sans:wght@400;600;700&family=Arimo:wght@400;700&display=swap">
<style>
  :root {
    --header-bg: #1d1917;
    --accent-red: #b30d0d;
    --nav-active: #ff1a1a;
    --white: #ffffff;
    --ink: #111111;
    --muted: #555555;
    --section-rose: #c7656d;
    --section-rose-deep: #a9505d;
    --section-dusk: #5b5f80;
    --social: #9aa6c9;
  }
  * { margin: 0; padding: 0; box-sizing: border-box; }
  html, body { width: 1120px; height: 1200px; overflow: hidden; background: var(--white); }
  body { position: relative; font-family: "Open Sans", sans-serif; color: var(--ink); }

  /* Header */
  .site-header {
    position: absolute; left: 0; top: 0; width: 1120px; height: 80px;
    background: var(--header-bg); border-bottom: 2px solid var(--accent-red);
  }
  .brand { position: absolute; left: 148px; top: 18px; display: flex; align-items: center; gap: 8px; }
  .brand-dot { width: 16px; height: 16px; border-radius: 50%; background: var(--accent-red); }
  .brand-name { font-family: "Open Sans", sans-serif; font-weight: 600; font-size: 28px; color: var(--white); letter-spacing: 0.5px; }
  .top-links { position: absolute; right: 160px; top: 17px; display: flex; align-items: center; gap: 14px; }
  .top-links a { font-family: "Arimo", sans-serif; font-weight: 700; font-size: 10.5px; color: var(--white); text-decoration: none; }
  .social { display: flex; gap: 8px; margin-left: 2px; }
  .social span { width: 17px; height: 17px; background: var(--social); display: block; }
  .main-nav { position: absolute; left: 437px; top: 52px; display: flex; align-items: center; }
  .main-nav a { font-family: "Arimo", sans-serif; font-size: 10.5px; color: var(--white); text-decoration: none; margin-right: 28px; letter-spacing: 0.2px; }
  .main-nav a.is-active { color: var(--nav-active); font-weight: 700; }
  .main-nav .divider { width: 1px; height: 14px; background: var(--white); margin: 0 12px 0 -8px; }
  .main-nav svg { display: block; }

  /* Hero */
  .hero { position: absolute; left: 0; top: 80px; width: 1120px; height: 460px; overflow: hidden; }
  .hero-photo {
    position: absolute; inset: 0;
    background: linear-gradient(100deg, #6e4a48 0%, #c9a692 30%, #e7cfc1 50%, #d9a38c 70%, #7a5a4a 100%);
  }
  .hero-arrow { position: absolute; top: 195px; }
  .hero-arrow.prev { left: 66px; }
  .hero-arrow.next { left: 1030px; opacity: 0.45; }
  .hero-content { position: absolute; left: 169px; top: 230px; width: 460px; }
  .hero-title { font-weight: 600; font-size: 37px; line-height: 42px; color: var(--accent-red); text-transform: uppercase; }
  .hero-text { font-family: "Arimo", sans-serif; font-size: 11.5px; line-height: 14.5px; margin-top: 8px; }
  .hero-actions { display: flex; gap: 11px; margin-top: 16px; margin-left: 4px; }
  .btn-outline {
    width: 187px; height: 41px; display: flex; align-items: center; justify-content: center;
    font-weight: 600; font-size: 18px; text-transform: uppercase; text-decoration: none; background: transparent;
  }
  .btn-outline.login { border: 1px solid var(--accent-red); color: var(--accent-red); }
  .btn-outline.join { border: 1px solid var(--ink); color: var(--ink); }
  .slider-dots { display: flex; gap: 2px; margin-top: 24px; margin-left: 4px; }
  .slider-dots span { width: 8px; height: 8px; border-radius: 50%; background: #f1f1f1; border: 1px solid #ccc; }
  .slider-dots span.is-current { background: var(--accent-red); border-color: var(--accent-red); }

  /* Welcome */
  .welcome { position: absolute; left: 0; top: 540px; width: 1120px; height: 217px; text-align: center; }
  .welcome h2 { font-weight: 600; font-size: 35px; color: var(--accent-red); margin-top: 40px; letter-spacing: 0.5px; }
  .welcome p { width: 740px; margin: 10px auto 0; font-size: 12.4px; line-height: 14.5px; }

  /* Finder */
  .finder {
    position: absolute; left: 0; top: 757px; width: 1120px; height: 349px; color: var(--white);
    background:
      radial-gradient(ellipse 300px 120px at 180px 300px, rgba(91,95,128,0.55), transparent 70%),
      radial-gradient(ellipse 260px 90px at 520px 40px, rgba(91,95,128,0.5), transparent 70%),
      radial-gradient(ellipse 260px 110px at 1040px 180px, rgba(91,95,128,0.45), transparent 70%),
      linear-gradient(180deg, var(--section-rose) 0%, var(--section-rose-deep) 100%);
  }
  .finder-figure {
    position: absolute; left: 755px; top: 50px; width: 180px; height: 245px;
    background: radial-gradient(ellipse at center, rgba(170,30,40,0.55) 0%, rgba(230,170,175,0.35) 55%, transparent 75%);
  }
  .finder-body { position: absolute; left: 158px; top: 40px; width: 520px; }
  .finder h2 { font-weight: 600; font-size: 36px; line-height: 44px; text-transform: uppercase; }
  .finder-text { font-family: "Arimo", sans-serif; font-size: 11.5px; line-height: 14.5px; margin: 10px 0 0 4px; }
  .form-row { display: flex; align-items: center; margin-left: 3px; font-size: 16px; }
  .form-row.first { margin-top: 27px; }
  .form-row.second { margin-top: 21px; }
  .field {
    height: 34px; background: var(--white); color: var(--muted); font-size: 16px;
    display: flex; align-items: center; font-family: "Arimo", sans-serif;
  }
  .field.select { justify-content: space-between; padding: 0 8px 0 11px; }
  .field.select::after { content: ""; border: 4px solid transparent; border-top: 4px solid var(--muted); margin-top: 4px; }
  .field.number { width: 62px; justify-content: center; }
  .select-gender { width: 150px; margin-left: 7px; }
  .select-city { width: 106px; margin-left: 8px; padding-left: 8px; }
  .label-gap { margin-left: 26px; }
  .form-row .to { margin: 0 10px; }
  .form-row .near { margin-left: 12px; }
  .form-row .age { margin-right: 10px; }
  .btn-start {
    display: inline-flex; align-items: center; justify-content: center; margin: 27px 0 0 2px;
    width: 154px; height: 34px; border: 1.5px solid var(--white); color: var(--white);
    font-weight: 600; font-size: 17px; text-transform: uppercase; text-decoration: none;
  }

  /* Footer */
  .site-footer { position: absolute; left: 0; top: 1106px; width: 1120px; height: 94px; }
  .copyright { position: absolute; left: 165px; top: 46px; font-family: "Arimo", sans-serif; font-size: 10.5px; color: #444; }
  .site-footer .social { position: absolute; left: 893px; top: 45px; gap: 8px; }
  .site-footer .social span { background: #a9bde6; }
</style>
</head>
<body>
  <header class="site-header">
    <div class="brand"><span class="brand-dot"></span><span class="brand-name">Alpendate</span></div>
    <div class="top-links">
      <a href="#">LOGIN</a>
      <a href="#">GET REGISTERED</a>
      <div class="social"><span></span><span></span><span></span></div>
    </div>
    <nav class="main-nav">
      <a href="#" class="is-active">HOME</a>
      <a href="#">JOIN</a>
      <a href="#">SEARCH</a>
      <a href="#">HELP</a>
      <a href="#">EVENTS</a>
      <a href="#">NEWS</a>
      <a href="#">SUCCESS STORIES</a>
      <span class="divider"></span>
      <svg width="12" height="12" viewBox="0 0 12 12" aria-label="Search"><circle cx="5" cy="5" r="3.8" fill="none" stroke="#fff" stroke-width="1.4"/><line x1="7.8" y1="7.8" x2="11" y2="11" stroke="#fff" stroke-width="1.5"/></svg>
    </nav>
  </header>

  <section class="hero">
    <div class="hero-photo" role="img" aria-label="Photo of a smiling couple sharing coffee in a warmly lit café"></div>
    <svg class="hero-arrow prev" width="26" height="26" viewBox="0 0 26 26" aria-label="Previous slide"><circle cx="13" cy="13" r="11.5" fill="none" stroke="#fff" stroke-width="2"/><circle cx="13" cy="13" r="8" fill="#fff"/><path d="M16 13H10M12.5 10L9.5 13L12.5 16" fill="none" stroke="#6e4a48" stroke-width="1.8"/></svg>
    <svg class="hero-arrow next" width="26" height="26" viewBox="0 0 26 26" aria-label="Next slide"><circle cx="13" cy="13" r="11.5" fill="none" stroke="#fff" stroke-width="2"/><circle cx="13" cy="13" r="8" fill="#fff"/><path d="M10 13H16M13.5 10L16.5 13L13.5 16" fill="none" stroke="#7a5a4a" stroke-width="1.8"/></svg>
    <div class="hero-content">
      <h1 class="hero-title">Get smart about online dating.</h1>
      <p class="hero-text">Lorem ipsum dolor sit amet, consectetuer adipiscing elit, sed diam nonummy nibh euismod tincidunt ut laoreet dolore magna aliquam erat volutpat.</p>
      <div class="hero-actions">
        <a href="#" class="btn-outline login">Login</a>
        <a href="#" class="btn-outline join">Join now</a>
      </div>
      <div class="slider-dots"><span></span><span></span><span class="is-current"></span><span></span><span></span></div>
    </div>
  </section>

  <section class="welcome">
    <h2>WELCOME</h2>
    <p>Lorem ipsum dolor sit amet, consectetuer adipiscing elit, sed diam nonummy nibh euismod tincidunt ut laoreet dolore magna aliquam erat volutpat. Ut wisi enim ad minim veniam, quis nostrud exerci tation ullamcorper suscipit lobortis nisl ut aliquip ex ea commodo consequat. Duis autem vel eum iriure dolor in hendrerit in vulputate velit esse molestie consequat, vel illum dolore eu feugiat nulla facilisis at vero eros et accumsan et iusto odio dignissim qui blandit praesent luptatum zzril delenit augue duis dolore te feugait nulla facilisi.</p>
  </section>

  <section class="finder">
    <div class="finder-figure" role="img" aria-label="Illustration of a winged figure in a red dress holding a bow, standing on a cloud"></div>
    <div class="finder-body">
      <h2>Find someone to talk to.</h2>
      <p class="finder-text">Lorem ipsum dolor sit amet, consectetuer adipiscing elit, sed diam nonummy nibh euismod tincidunt ut laoreet dolore magna aliquam erat volutpat.</p>
      <div class="form-row first">
        <span>I’m a Men.</span>
        <span class="label-gap">Interested in</span>
        <div class="field select select-gender">Women</div>
      </div>
      <div class="form-row second">
        <span class="age">age</span>
        <div class="field number">20</div>
        <span class="to">to</span>
        <div class="field number">35</div>
        <span class="near">NEAR</span>
        <div class="field select select-city">Lausannes</div>
      </div>
      <a href="#" class="btn-start">Get started</a>
    </div>
  </section>

  <footer class="site-footer">
    <p class="copyright">© Copyright 2014 Alpendate. All rights reserved.</p>
    <div class="social"><span></span><span></span><span></span></div>
  </footer>
</body>
</html>
```